BUCHCOVER - SACHBUCH inkl. Promotionkarte
Vel Orvano suchte ein neues Design in der Kategorie Buch-/eBook-Cover und hat ein Projekt auf gestaltwerkstatt.example gestartet.
Zielgruppe
www.LumaTrekk.example
Zielgruppe: Privatpersonen, Sozialarbeiter, Therapeuten
Aufgabenstellung
Buchtitel:
DAS LICHT HINTER DEN WOLKEN
Untertitel: Ein Erlebnisbericht
Autorin:
Lydia Femmert
Verlag:
VEL ORVANO VERLAG
(VERLAGSLOGO)
Softcoverbuch
Titelseite, Seitenleiste, Rückseite mit Blindtext für Klappentext und Barcode
DIN 5
Schlicht und sachlich gehalten, ohne esoterische Elemente.
Promotionkarte mit Bestellmöglichkeit in Din Lang Vorderseite + Rückseite

```html
<!DOCTYPE html>
<html lang="de">
<head>
<meta charset="utf-8">
<title>Das Licht hinter den Wolken – Promotionkarte</title>
<link rel="stylesheet" href="https://fonts.googleapis.com/css2?family=Crimson+Pro:ital,wght@0,400;0,600;0,700;1,400;1,700&display=swap">
<style>
  :root {
    --navy: #1d2750;
    --blue: #0f5fa4;
    --blue-text: #1a62a8;
    --panel: #dfe6f0;
    --white: #ffffff;
    --ink: #1d2236;
    --rule: #b9bfc9;
    --page: #f1f1f1;
  }
  * { box-sizing: border-box; margin: 0; padding: 0; }
  html, body { width: 1200px; height: 848px; overflow: hidden; background: var(--white); }
  body { position: relative; font-family: "Crimson Pro", Georgia, serif; color: var(--ink); }

  .card { position: absolute; left: 303px; width: 600px; height: 300px; overflow: hidden; box-shadow: 0 1px 4px rgba(0,0,0,.25); }
  .card--front { top: 104px; background: linear-gradient(180deg, var(--navy) 0 98px, #1166ad 98px, #0e4f8e 190px, var(--navy) 300px); }
  .card--back { top: 446px; background: var(--white); }

  .title { position: absolute; left: 15px; top: 9px; color: var(--white); font-weight: 600; font-size: 27px; line-height: 33px; letter-spacing: 1.5px; white-space: nowrap; text-shadow: 1px 1px 3px rgba(0,0,0,.5); }
  .subtitle { position: absolute; left: 160px; top: 52px; color: var(--white); font-style: italic; font-size: 16.5px; line-height: 20px; white-space: nowrap; }

  .portrait { position: absolute; left: 15px; top: 92px; width: 101px; height: 151px; border: 4px solid var(--white); background: linear-gradient(160deg, #cfd6de, #8a8f96 55%, #2a2a2e); }
  .bio { position: absolute; left: 132px; top: 108px; width: 180px; color: var(--white); }
  .bio__name { font-weight: 700; font-size: 15px; line-height: 17px; }
  .bio__text { font-size: 9.4px; line-height: 12.1px; }
  .bio__url { margin-top: 4px; font-style: italic; font-weight: 700; font-size: 9.5px; }
  .signature { position: absolute; left: 130px; top: 208px; width: 105px; height: 46px; background: linear-gradient(90deg, rgba(255,255,255,.18), rgba(255,255,255,.05)); border-radius: 3px; }
  .release { position: absolute; left: 15px; top: 258px; color: var(--white); font-weight: 700; font-size: 23px; line-height: 28px; white-space: nowrap; }

  .book { position: absolute; overflow: visible; }
  .book--front { left: 290px; top: 40px; width: 270px; height: 250px; }
  .book--back { left: 216px; top: 100px; width: 175px; height: 162px; }

  .badge { position: absolute; border-radius: 50%; background: var(--white); box-shadow: 2px 3px 6px rgba(0,0,0,.35); color: var(--blue-text); font-weight: 700; display: flex; align-items: center; justify-content: center; }
  .badge--front { left: 457px; top: 18px; width: 100px; height: 100px; font-size: 40px; }
  .badge--back { left: 315px; top: 109px; width: 56px; height: 56px; font-size: 22px; }

  .imprint { position: absolute; text-align: center; font-weight: 400; line-height: 1; white-space: nowrap; }
  .imprint--front { left: 528px; top: 272px; width: 66px; color: var(--white); font-size: 9px; letter-spacing: .5px; }
  .imprint--front .imprint__sub { font-size: 5.5px; letter-spacing: 2px; }
  .imprint--back { left: 339px; top: 274px; width: 40px; color: var(--navy); font-size: 6.5px; }
  .imprint--back .imprint__sub { font-size: 4px; letter-spacing: 1px; }

  .order { position: absolute; left: 0; top: 0; width: 389px; height: 300px; background: var(--panel); }
  .order__lead { position: absolute; left: 21px; top: 15px; font-weight: 700; font-size: 12.5px; line-height: 14px; white-space: nowrap; }
  .order__lead .price { color: var(--blue-text); }
  .order__qty { display: inline-block; width: 26px; height: 20px; background: var(--white); vertical-align: -4px; margin: 0 5px; }
  .field { position: absolute; left: 16px; width: 229px; background: var(--white); color: var(--blue-text); font-weight: 700; font-size: 9.8px; padding: 3px 5px; }
  .order__url { position: absolute; right: 56px; top: 273px; font-style: italic; color: var(--blue-text); font-size: 8.5px; white-space: nowrap; }
  .divider { position: absolute; left: 386px; top: 98px; width: 3px; height: 142px; background: var(--navy); }

  .stamp { position: absolute; left: 528px; top: 17px; width: 55px; height: 72px; border: 1px solid #777; font-size: 7px; line-height: 8px; text-align: center; padding-top: 24px; }
  .address-line { position: absolute; left: 403px; width: 150px; height: 1px; background: var(--rule); }
</style>
</head>
<body>

<section class="card card--front">
  <h1 class="title">DAS LICHT HINTER DEN<br>WOLKEN</h1>
  <p class="subtitle">Ein Erlebnisbericht von<br>Lydia Femmert</p>

  <div class="portrait" role="img" aria-label="Porträtfoto der Autorin"></div>

  <div class="bio">
    <p class="bio__name">Lydia Femmert</p>
    <p class="bio__text">ist systemischer Coach, Journalistin, Solvara-Heilerin und LUMA-Lehrerin. Sie ist an der Entwicklung und Konzeption der LUMA-Intensiv-Seminare beteiligt und für die Publikations- und Pressearbeit zuständig.</p>
    <p class="bio__url">www.LumaTrekk.example</p>
  </div>
  <div class="signature" role="img" aria-label="Handschriftliche Unterschrift der Autorin"></div>

  <p class="release">Ab 1. August 2014 im Handel</p>

  <svg class="book book--front" viewBox="0 0 270 250">
    <defs>
      <linearGradient id="photoFront" x1="0" y1="0" x2="0" y2="1">
        <stop offset="0" stop-color="#b8c0c8"/>
        <stop offset=".6" stop-color="#7a7f86"/>
        <stop offset="1" stop-color="#3a3c42"/>
      </linearGradient>
    </defs>
    <polygon points="9,39 157,6 256,187 82,249" fill="var(--page)"/>
    <polygon points="9,39 157,6 253,180 79,240" fill="var(--navy)"/>
    <polygon points="9,39 157,6 215,110 51,160" fill="url(#photoFront)" role="img" aria-label="Porträtfoto der Autorin auf dem Buchcover"/>
    <polygon points="51,160 215,110 221,123 56,174" fill="var(--white)"/>
    <text x="136" y="146" transform="rotate(-17 136 146)" text-anchor="middle" font-family="Crimson Pro, Georgia, serif" font-weight="600" font-size="11" letter-spacing="1" fill="var(--navy)">LYDIA FEMMERT</text>
    <text x="146" y="163" transform="rotate(-17 146 163)" text-anchor="middle" font-family="Crimson Pro, Georgia, serif" font-weight="600" font-size="8.5" fill="var(--white)">Das Licht hinter den Wolken</text>
    <text x="150" y="173" transform="rotate(-17 150 173)" text-anchor="middle" font-family="Crimson Pro, Georgia, serif" font-style="italic" font-size="5" fill="var(--white)">Ein Erlebnisbericht</text>
  </svg>

  <div class="badge badge--front">NEU</div>

  <p class="imprint imprint--front">VEL ORVANO<br><span class="imprint__sub">VERLAG</span></p>
</section>

<section class="card card--back">
  <div class="order">
    <p class="order__lead">Ich bestelle<span class="order__qty"></span>Exemplare zum Preis von je <span class="price">13,80 Euro</span> zuzüglich<br>2 Euro Versandkostenkauschale.</p>

    <div class="field" style="top:54px;height:20px">Name</div>
    <div class="field" style="top:82px;height:16px;padding-top:2px">Straße</div>
    <div class="field" style="top:108px;height:16px;padding-top:2px">PLZ</div>
    <div class="field" style="top:135px;height:16px;padding-top:2px">Ort</div>
    <div class="field" style="top:161px;height:16px;padding-top:2px">Telefon</div>
    <div class="field" style="top:187px;height:16px;padding-top:2px">E-Mail</div>
    <div class="field" style="top:214px;height:16px;padding-top:2px">Datum</div>
    <div class="field" style="top:240px;height:44px">Unterschrift</div>

    <svg class="book book--back" viewBox="0 0 270 250">
      <defs>
        <linearGradient id="photoBack" x1="0" y1="0" x2="0" y2="1">
          <stop offset="0" stop-color="#b8c0c8"/>
          <stop offset=".6" stop-color="#7a7f86"/>
          <stop offset="1" stop-color="#3a3c42"/>
        </linearGradient>
      </defs>
      <polygon points="9,39 157,6 256,187 82,249" fill="var(--page)"/>
      <polygon points="9,39 157,6 253,180 79,240" fill="var(--navy)"/>
      <polygon points="9,39 157,6 215,110 51,160" fill="url(#photoBack)" role="img" aria-label="Porträtfoto der Autorin auf dem Buchcover"/>
      <polygon points="51,160 215,110 221,123 56,174" fill="var(--white)"/>
      <text x="136" y="146" transform="rotate(-17 136 146)" text-anchor="middle" font-family="Crimson Pro, Georgia, serif" font-weight="600" font-size="11" letter-spacing="1" fill="var(--navy)">LYDIA FEMMERT</text>
      <text x="146" y="163" transform="rotate(-17 146 163)" text-anchor="middle" font-family="Crimson Pro, Georgia, serif" font-weight="600" font-size="8.5" fill="var(--white)">Das Licht hinter den Wolken</text>
    </svg>
    <div class="badge badge--back">NEU</div>

    <p class="order__url">www.LumaTrekk.example</p>
    <p class="imprint imprint--back">VEL ORVANO<br><span class="imprint__sub">VERLAG</span></p>
  </div>
  <div class="divider"></div>

  <div class="stamp">Bitte<br>ausreichend<br>frankieren</div>
  <div class="address-line" style="top:127px"></div>
  <div class="address-line" style="top:158px"></div>
  <div class="address-line" style="top:187px"></div>
  <div class="address-line" style="top:218px"></div>
</section>

</body>
</html>
```